Kito Rise and Glow Dance Fitness-KRGDF

Catchy POSTER .
The poster must attract both eyes of all ages looking for fitness,Ritmoflex to have fun, professional dance training and Yoga.

Target Market(s)

Dancers and Non Dancers

Industry/Entity Type

Training

Requirements
Must have
• Kito Dance Ensemble
Presents
KITO RISE AND GLOW DANCE FITNESS

African Dance
Modern/Samtidsdans,
Yoga
Ritmoflex
Hip Hop
Massage and repertoire classes.

Venue:Vetlefjord Kulturhus
Call 47351208 to register/TEXT
kitoarts@kitomail.example
www.kitoarts-example.org
Nice to have
• OG creativity...think outside the box
Should not have
• Please NO cartoon charectors!!! or BALLET DANCING LIONS!!!

```html
<!DOCTYPE html>
<html lang="en">
<head>
<meta charset="utf-8">
<title>Kito Rise and Glow Dance Fitness – Poster</title>
<link rel="stylesheet" href="https://fonts.googleapis.com/css2?family=Montserrat:wght@300;400;600;700&family=Oswald:wght@500;600&family=Pinyon+Script&display=swap">
<style>
  :root {
    --page: #ffffff;
    --ink-blue: #a9dcf2;
    --accent-pink: #ea0f4c;
    --band-text: #fde6a3;
    --deep-red: #5e0a1f;
    --mid-red: #b3163c;
    --glow-pink: #ff4f95;
    --hot-core: #ffd1e4;
    --nebula-orange: #ff7a3c;
    --nebula-violet: #6a3fd0;
    --streak: #fff1c8;
  }
  html, body {
    margin: 0;
    width: 1200px;
    height: 1000px;
    overflow: hidden;
    background: var(--page);
  }
  .poster {
    position: absolute;
    left: 246px;
    top: 0;
    width: 704px;
    height: 1000px;
    display: block;
  }
  .presenter { font-family: "Pinyon Script", cursive; fill: var(--ink-blue); }
  .title-side { font-family: "Oswald", sans-serif; font-weight: 600; fill: var(--ink-blue); }
  .title-main { font-family: "Oswald", sans-serif; font-weight: 600; fill: var(--ink-blue); }
  .title-sub { font-family: "Montserrat", sans-serif; font-weight: 700; fill: var(--ink-blue); }
  .register { font-family: "Montserrat", sans-serif; font-weight: 300; fill: var(--ink-blue); }
  .register .phone { font-weight: 700; }
  .coproducer { font-family: "Montserrat", sans-serif; font-weight: 700; fill: var(--ink-blue); }
  .class-list { font-family: "Montserrat", sans-serif; font-weight: 400; fill: var(--band-text); }
  .web { font-family: "Montserrat", sans-serif; font-weight: 700; fill: var(--ink-blue); }
  .web .tld { font-weight: 400; }
  .email { font-family: "Montserrat", sans-serif; font-weight: 400; fill: var(--ink-blue); }
  .accent { fill: var(--accent-pink); }
  .streak { fill: none; stroke: var(--streak); stroke-width: 2.2; }
  .streak-glow { fill: none; stroke: #ffd27a; stroke-width: 7; opacity: .35; }
  .ray { fill: var(--glow-pink); opacity: .16; }
</style>
</head>
<body>
<svg class="poster" viewBox="0 0 704 1000" xmlns="http://www.w3.org/2000/svg">
  <defs>
    <radialGradient id="bg-glow" cx="0.55" cy="0.3" r="0.85">
      <stop offset="0" stop-color="#f02a6a"/>
      <stop offset="0.3" stop-color="#c8163f"/>
      <stop offset="0.65" stop-color="var(--deep-red)"/>
      <stop offset="1" stop-color="#2e0410"/>
    </radialGradient>
    <radialGradient id="core-burst" cx="0.5" cy="0.5" r="0.5">
      <stop offset="0" stop-color="var(--hot-core)" stop-opacity=".9"/>
      <stop offset="0.3" stop-color="var(--glow-pink)" stop-opacity=".75"/>
      <stop offset="1" stop-color="var(--glow-pink)" stop-opacity="0"/>
    </radialGradient>
    <radialGradient id="nebula-orange" cx="0.5" cy="0.5" r="0.5">
      <stop offset="0" stop-color="var(--nebula-orange)" stop-opacity=".75"/>
      <stop offset="1" stop-color="var(--nebula-orange)" stop-opacity="0"/>
    </radialGradient>
    <radialGradient id="nebula-violet" cx="0.5" cy="0.5" r="0.5">
      <stop offset="0" stop-color="var(--nebula-violet)" stop-opacity=".7"/>
      <stop offset="1" stop-color="var(--nebula-violet)" stop-opacity="0"/>
    </radialGradient>
    <radialGradient id="dark-corner" cx="0.5" cy="0.5" r="0.5">
      <stop offset="0" stop-color="#12020a" stop-opacity=".85"/>
      <stop offset="1" stop-color="#12020a" stop-opacity="0"/>
    </radialGradient>
    <radialGradient id="dancers-tone" cx="0.5" cy="0.45" r="0.5">
      <stop offset="0" stop-color="#c98a7a" stop-opacity=".85"/>
      <stop offset="0.45" stop-color="#8f3a4c" stop-opacity=".7"/>
      <stop offset="0.8" stop-color="#3a1018" stop-opacity=".35"/>
      <stop offset="1" stop-color="#3a1018" stop-opacity="0"/>
    </radialGradient>
    <filter id="soft" x="-20%" y="-20%" width="140%" height="140%">
      <feGaussianBlur stdDeviation="3"/>
    </filter>
  </defs>

  <rect class="backdrop" width="704" height="1000" fill="url(#bg-glow)"/>

  <g class="burst-rays">
    <polygon class="ray" points="380,260 0,40 0,110"/>
    <polygon class="ray" points="380,260 90,0 170,0"/>
    <polygon class="ray" points="380,260 560,0 640,0"/>
    <polygon class="ray" points="380,260 704,150 704,230"/>
    <polygon class="ray" points="380,260 704,400 704,470"/>
    <polygon class="ray" points="380,260 0,330 0,390"/>
    <polygon class="ray" points="380,260 300,0 350,0"/>
  </g>

  <g class="nebula">
    <ellipse cx="110" cy="110" rx="150" ry="110" fill="url(#nebula-orange)"/>
    <ellipse cx="40" cy="240" rx="130" ry="90" fill="url(#nebula-violet)"/>
    <ellipse cx="380" cy="250" rx="300" ry="240" fill="url(#core-burst)"/>
    <ellipse cx="0" cy="0" rx="200" ry="140" fill="url(#dark-corner)"/>
    <ellipse cx="704" cy="10" rx="220" ry="150" fill="url(#dark-corner)"/>
  </g>

  <g class="dancers-photo" role="img" aria-label="Photo of two fitness dancers posing: a woman in a pink top and a man in a black tank top lifting a dumbbell">
    <ellipse cx="340" cy="290" rx="230" ry="240" fill="url(#dancers-tone)"/>
  </g>

  <g class="light-streaks">
    <g filter="url(#soft)">
      <path class="streak-glow" d="M0 60 C170 250 320 430 460 470 C560 498 640 420 704 330"/>
      <path class="streak-glow" d="M0 320 C170 390 360 470 520 440 C610 420 660 320 704 290"/>
      <path class="streak-glow" d="M704 40 C600 120 510 240 450 340"/>
    </g>
    <path class="streak" d="M0 60 C170 250 320 430 460 470 C560 498 640 420 704 330"/>
    <path class="streak" d="M0 320 C170 390 360 470 520 440 C610 420 660 320 704 290"/>
    <path class="streak" d="M0 200 C130 270 260 340 400 370 C500 392 560 360 620 340"/>
    <path class="streak" d="M130 0 C190 160 300 310 430 390"/>
    <path class="streak" d="M704 40 C600 120 510 240 450 340"/>
    <path class="streak" d="M704 120 C620 170 540 210 470 250"/>
    <path class="streak" d="M210 440 C300 480 420 490 560 420"/>
  </g>

  <rect class="accent" x="54" y="481" width="46" height="41"/>
  <rect class="accent" x="608" y="481" width="43" height="41"/>
  <text class="presenter" x="354" y="520" font-size="40" text-anchor="middle" textLength="490" lengthAdjust="spacingAndGlyphs">Kito Dance Ensemble presents...</text>

  <text class="title-side" font-size="44" text-anchor="middle" transform="translate(90 580) rotate(-90)" textLength="100" lengthAdjust="spacingAndGlyphs">KITO</text>
  <text class="title-main" x="102" y="628" font-size="130" textLength="547" lengthAdjust="spacingAndGlyphs">RISE AND GLOW</text>
  <text class="title-sub" x="54" y="697" font-size="76" textLength="595" lengthAdjust="spacingAndGlyphs">DANCE FITNESS</text>

  <rect class="accent" x="54" y="712" width="595" height="2"/>

  <text class="register" x="352" y="762" font-size="40" text-anchor="middle" textLength="590" lengthAdjust="spacingAndGlyphs">Call/Text <tspan class="phone">47 35 1208</tspan> to register</text>

  <polygon class="accent" points="140,781 152,788 140,795"/>
  <text class="coproducer" x="352" y="795" font-size="17" text-anchor="middle" textLength="396" lengthAdjust="spacingAndGlyphs">CO-PRODUCED by VETLEFJORD KULTURHUS</text>
  <polygon class="accent" points="564,781 552,788 564,795"/>

  <rect class="accent" x="0" y="828" width="704" height="60"/>
  <text class="class-list" x="352" y="855" font-size="22" text-anchor="middle" textLength="592" lengthAdjust="spacingAndGlyphs">AFRICAN DANCE • MODERN/SAMTIDSDANS • MASSAGE</text>
  <text class="class-list" x="352" y="881" font-size="22" text-anchor="middle" textLength="560" lengthAdjust="spacingAndGlyphs">RITMOFLEX • YOGA • HIP HOP • REPERTOIRE CLASSES</text>

  <text class="web" x="352" y="932" font-size="20" text-anchor="middle">KitoArts-example<tspan class="tld">.org</tspan></text>
  <text class="email" x="352" y="955" font-size="15" text-anchor="middle">KitoArts@kitomail.example</text>
</svg>
</body>
</html>
```